Cover needed for book, Wedded to the Fellow Who Drifted Out to Sea

Cover should use the attached photograph, with the groom faded in some way, to represent the concept in the title. Overall look should tell readers the book is in the genre of Marian's Embers, Never Send Us Back Home etc. Book is memoir of Edith, who was married to a man who had obsessive-compulsive disorder when little was known about the condition.

Text should be

Wedded to the Fellow Who Drifted Out to Sea
The true story of how obsession tore a family apart
By Edith Harcombe

```html
<!DOCTYPE html>
<html lang="en">
<head>
<meta charset="utf-8">
<title>Wedded to the Fellow Who Drifted Out to Sea — Book Cover</title>
<link rel="stylesheet" href="https://fonts.googleapis.com/css2?family=Raleway:wght@300;400;800;900&display=swap">
<style>
  :root {
    --backdrop: #5b4b3b;
    --showcase-white: #ffffff;
    --paper: #b3a592;
    --paper-light: #c1b3a1;
    --title-red: #c7282b;
    --ink: #2b2926;
    --ink-soft: #3a3733;
    --frame-white: #efece6;
    --photo-dark: #3c3c3c;
    --photo-mid: #8e8e8c;
    --photo-light: #d6d5d2;
  }
  * { margin: 0; padding: 0; box-sizing: border-box; }
  html, body {
    width: 1200px;
    height: 3108px;
    overflow: hidden;
    background: var(--backdrop);
  }
  .canvas {
    position: relative;
    width: 1200px;
    height: 3108px;
    background: var(--backdrop);
  }
  .showcase-top {
    position: absolute;
    left: 0;
    top: 0;
    width: 1200px;
    height: 1320px;
    background: var(--showcase-white);
  }
  .showcase-bottom {
    position: absolute;
    left: 0;
    top: 1320px;
    width: 1200px;
    height: 1788px;
    background: var(--backdrop);
  }
  .book-cover {
    position: absolute;
    width: 1056px;
    height: 1584px;
    background: radial-gradient(ellipse at 50% 40%, var(--paper-light) 0%, var(--paper) 75%);
    font-family: 'Raleway', sans-serif;
    text-align: center;
    transform-origin: top left;
  }
  .book-cover--main {
    left: 72px;
    top: 104px;
    box-shadow: 0 6px 20px rgba(0,0,0,0.3);
  }
  .book-cover--preview {
    left: 150px;
    top: 88px;
    transform: scale(0.697);
    box-shadow: 14px 14px 40px rgba(0,0,0,0.25);
  }
  .book-cover h1 { font-weight: normal; }
  .title-lead,
  .title-rest,
  .tagline-lead,
  .tagline-rest,
  .author-name {
    position: absolute;
    left: 0;
    width: 100%;
    line-height: 1;
    text-transform: uppercase;
    white-space: nowrap;
  }
  .title-lead {
    top: 180px;
    font-weight: 900;
    font-size: 56px;
    letter-spacing: 1px;
    color: var(--title-red);
  }
  .title-rest {
    top: 280px;
    font-weight: 300;
    font-size: 47px;
    letter-spacing: 1px;
    color: var(--ink-soft);
  }
  .photo-frame {
    position: absolute;
    left: 188px;
    top: 384px;
    width: 680px;
    height: 860px;
    background: var(--frame-white);
    padding: 22px;
    box-shadow: 0 4px 14px rgba(0,0,0,0.28);
  }
  .wedding-photo {
    width: 100%;
    height: 100%;
    background:
      linear-gradient(90deg, rgba(255,255,255,0.45) 0%, rgba(255,255,255,0.25) 35%, rgba(255,255,255,0) 55%),
      linear-gradient(180deg, var(--photo-light) 0%, var(--photo-mid) 55%, var(--photo-dark) 100%);
  }
  .tagline-lead {
    top: 1306px;
    font-weight: 800;
    font-size: 42px;
    color: var(--ink);
  }
  .tagline-rest {
    top: 1352px;
    font-weight: 300;
    font-size: 41px;
    color: var(--ink);
  }
  .author-name {
    top: 1424px;
    font-weight: 800;
    font-size: 74px;
    letter-spacing: 1px;
    color: var(--title-red);
  }
</style>
</head>
<body>
  <main class="canvas">
    <section class="showcase-top">
      <div class="book-cover book-cover--preview" aria-hidden="true">
        <p class="title-lead">Wedded to the Fellow</p>
        <p class="title-rest">Who Drifted Out to Sea</p>
        <div class="photo-frame">
          <div class="wedding-photo"></div>
        </div>
        <p class="tagline-lead">The True Story of</p>
        <p class="tagline-rest">How Obsession Tore a Family Apart</p>
        <p class="author-name">Edith Harcombe</p>
      </div>
    </section>
    <section class="showcase-bottom">
      <div class="book-cover book-cover--main">
        <h1>
          <span class="title-lead">Wedded to the Fellow</span>
          <span class="title-rest">Who Drifted Out to Sea</span>
        </h1>
        <div class="photo-frame">
          <div class="wedding-photo" role="img" aria-label="Black-and-white wedding photograph of a bride with bouquet and a groom in a dark suit before a lattice arch, the groom faded away"></div>
        </div>
        <p class="tagline-lead">The True Story of</p>
        <p class="tagline-rest">How Obsession Tore a Family Apart</p>
        <p class="author-name">Edith Harcombe</p>
      </div>
    </section>
  </main>
</body>
</html>
```